Stationery Refresh For Local Mortgage Broker

We want to modernise and standardise our stationery, including: letterhead, presentation folder, email signature and business card.

The new stationery should be a more modern and professional take on our existing colour scheme and brand. (We do not want a complete overhaul.) A folder of approved stock photos can be found here: https://files.cloudvaultex.com/share/7kTmQzR2wY9bLp4nVx3cHd8sJf6gNa1eU/view?usp=sharing

Our current website is: www.brellanfinco.com.au but we will be updating this to be consistent with our new stationery.

We are open to *very slight* tweaks to our logo if you feel it needs modernising, but overall we would like to maintain consistent colour scheme.

> Letterhead

418 Wenlock Parade,
Geelong, VIC, 3220
ABN: 37 158 402 963
Australian Credit License: 712893

(03) 5019 6284
www.brellanfinco.com.au

> Presentation Folder

418 Wenlock Parade,
Geelong, VIC, 3220
(03) 5019 6284
www.brellanfinco.com.au

ABN: 37 158 402 963

> Email Signature

Dylan Ferraway
Director
M. 0417 250 964
P. (03) 5019 6284
www.brellanfinco.com.au
418 Wenlock Parade,
Geelong, VIC, 3220

ABN: 37 158 402 963

(you can also include a photo if you like: https://brellanfinco.com.au/wp-content/uploads/2020/12/Dylan-Ferraway.png.webp)

> Business Card

Dylan Ferraway
Director
M. 0417 250 964
P. (03) 5019 6284
www.brellanfinco.com.au
418 Wenlock Parade,
Geelong, VIC, 3220

ABN: 37 158 402 963

Additional information...

If it's useful/relevant, the services we offer are: Home Loans, Investment Loans, Refinance, Debt Consolidation, Commercial Finance, Vehicle Loans
(You may choose to use this in any of the designs)

Target Market(s)

Home Buyers and Investors

Industry/Entity Type

Mortgage broking/property/real estate

Requirements
Must have
• At least somewhat consistent with our current site (yet meaningfully modernized)
Should not have
• dramatically different logo or colourscheme overhauls

```html
<!DOCTYPE html>
<html lang="en">
<head>
<meta charset="utf-8">
<title>Brellan Financial Services – Letterhead</title>
<link href="https://fonts.googleapis.com/css2?family=Open+Sans:wght@400&family=Roboto:wght@400&display=swap" rel="stylesheet">
<style>
  :root {
    --brand-red: #9b1b1f;
    --brand-grey: #58595b;
    --ink: #454545;
    --footer-ink: #2b2b2b;
    --paper: #f8f8f8;
    --backdrop: #dcdcdc;
  }
  * { box-sizing: border-box; margin: 0; padding: 0; }
  html, body { width: 1153px; height: 1200px; overflow: hidden; }
  body { background: var(--backdrop); position: relative; }

  .letterhead {
    position: absolute; left: 146px; top: 0;
    width: 860px; height: 1200px;
    background: var(--paper);
    font-family: "Open Sans", sans-serif;
    color: var(--ink);
  }

  .brand {
    position: absolute; top: 112px; left: 0; width: 100%;
    display: flex; justify-content: center; align-items: center; gap: 14px;
  }
  .brand-mark {
    width: 34px; height: 34px;
    background: var(--brand-red);
  }
  .brand-name {
    font-family: "Open Sans", sans-serif;
    font-weight: 400;
    font-size: 30px;
    line-height: 40px;
    color: var(--brand-red);
  }

  .letter-body {
    position: absolute; left: 77px; top: 292px; width: 704px;
    font-size: 15.5px; line-height: 23px;
  }
  .letter-body p { margin-bottom: 23px; text-align: justify; }
  .letter-body .salutation, .letter-body .closing { text-align: left; }

  .signature {
    position: absolute; left: 77px; top: 903px;
    width: 104px; height: 97px;
    background: linear-gradient(135deg, #e6e6e6, #d4d4d4);
    border-radius: 4px;
  }

  .contact {
    position: absolute; left: 0; top: 1098px; width: 100%;
    text-align: center;
    font-family: "Roboto", sans-serif;
    font-size: 16px; line-height: 21px;
    color: var(--footer-ink);
  }
  .contact .divider { color: var(--brand-red); padding: 0 2px; }
  .contact .icon { width: 13px; height: 13px; vertical-align: -1px; margin: 0 3px 0 4px; fill: var(--brand-red); }

  .footer-band { position: absolute; left: 0; bottom: 0; width: 860px; height: 20px; }
</style>
</head>
<body>
  <main class="letterhead">
    <header class="brand">
      <span class="brand-mark" aria-hidden="true"></span>
      <span class="brand-name">Brellan Financial Services</span>
    </header>

    <section class="letter-body">
      <p class="salutation">Dear customer,</p>
      <p>Lorem ipsum dolor sit amet, consectetur adipisicing elit, sed do eiusmod tempor incididunt ut labore et dolore magna aliqua. Ut enim ad minim veniam, quis nostrud exercitation ullamco laboris nisi ut aliquip ex ea commodo consequat. Duis aute irure dolor in reprehenderit in voluptate velit esse cillum dolore eu fugiat nulla pariatur. Excepteur sint occaecat cupidatat non proident, sunt in culpa qui officia deserunt mollit anim id est laborum.</p>
      <p>Lorem ipsum dolor sit amet, consectetur adipisicing elit, sed do eiusmod tempor incididunt ut labore et dolore magna aliqua. Ut enim ad minim veniam, quis nostrud exercitation ullamco laboris nisi ut aliquip ex ea commodo consequat. Duis aute irure dolor in reprehenderit in voluptate velit esse cillum dolore eu fugiat nulla pariatur. Excepteur sint occaecat cupidatat non proident, sunt in culpa qui officia deserunt mollit anim id est laborum.</p>
      <p>Lorem ipsum dolor sit amet, consectetur adipisicing elit, sed do eiusmod tempor incididunt ut labore et dolore magna aliqua. Ut enim ad minim veniam, quis nostrud exercitation ullamco laboris nisi ut aliquip ex ea commodo consequat. Duis aute irure dolor in reprehenderit in voluptate velit esse cillum dolore eu fugiat nulla pariatur. Excepteur sint occaecat cupidatat non proident, sunt in culpa qui officia deserunt mollit anim id est laborum.</p>
      <p>Lorem ipsum dolor sit amet, consectetur adipisicing elit, sed do eiusmod tempor incididunt ut labore et dolore magna aliqua. Ut enim ad minim veniam, quis nostrud exercitation ullamco laboris nisi ut aliquip ex ea commodo consequat. Duis aute irure dolor in reprehenderit.</p>
      <p class="closing">Yours Sincerely,</p>
    </section>

    <div class="signature" role="img" aria-label="Handwritten signature of the sender"></div>

    <footer class="contact">
      <div>418 Wenlock Parade, Geelong, VIC, 3220</div>
      <div>ABN: 37 158 402 963 <span class="divider">|</span> Australian Credit License: 712893</div>
      <div>
        <svg class="icon" viewBox="0 0 16 16" aria-hidden="true"><path d="M2 5c0-2 2-3 6-3s6 1 6 3v1h-3V4.5H5V6H2z"/><path d="M4 7h8l2 6H2z"/></svg>(03) 5019 6284
        <svg class="icon" viewBox="0 0 16 16" aria-hidden="true"><path d="M1 3h14v10H1z"/><path d="M1 3l7 5 7-5" fill="none" stroke="#f8f8f8" stroke-width="1.4"/></svg>info@brellanfinco.com.au
        <svg class="icon" viewBox="0 0 16 16" aria-hidden="true"><circle cx="8" cy="8" r="7"/><path d="M1 8h14M8 1c-3 3-3 11 0 14M8 1c3 3 3 11 0 14" fill="none" stroke="#f8f8f8" stroke-width="1"/></svg>www.brellanfinco.com.au
      </div>
    </footer>

    <svg class="footer-band" viewBox="0 0 860 20" preserveAspectRatio="none" aria-hidden="true">
      <polygon points="0,0 583,0 563,20 0,20" fill="var(--brand-red)"/>
      <polygon points="593,0 860,0 860,20 573,20" fill="var(--brand-grey)"/>
    </svg>
  </main>
</body>
</html>
```